Single Page Digital Brochure

We are a Sydney based finance company. We lend money to developers. Please see attached example of what we are looking to have produced. We just need a design which can be posted on LINKEDIN

Target Market(s)

Property Developers who are borrowing money

Industry/Entity Type

Finance

Requirements
Must have
• Australian relevant imagery.

TEXT TO INCLUDE:

New Offering from Ferngate Lending
Nice to have
• Design and colour scheme based around our logo (attached)

Please include the same text as the attachment

Please make the design based loosely on the attachment. But do not copy the attachement
Should not have
• Remove Text: 'Settle in under four days'

```html
<!DOCTYPE html>
<html lang="en">
<head>
<meta charset="utf-8">
<title>Ferngate Lending – New Offering</title>
<link href="https://fonts.googleapis.com/css2?family=Arimo:wght@400;700&family=Montserrat:wght@500;600;700&display=swap" rel="stylesheet">
<style>
  :root {
    --backdrop: #b5b5b5;
    --band-green: #284a38;
    --ink: #1d1d1d;
    --label-green: #2a5a40;
    --white: #ffffff;
    --photo-grey-light: #f4f4f4;
    --photo-grey-mid: #d7d7d7;
  }
  * { box-sizing: border-box; margin: 0; padding: 0; }
  html, body { width: 1200px; height: 900px; overflow: hidden; }
  body { background: var(--backdrop); position: relative; font-family: "Arimo", Arial, sans-serif; }

  .brochure {
    position: absolute; left: 68px; top: 93px; width: 1064px; height: 715px;
    background: var(--white);
  }

  /* Left brand panel */
  .brand-panel {
    position: absolute; left: 0; top: 0; width: 484px; height: 715px;
    overflow: hidden; color: var(--white);
  }
  .brand-panel__photo {
    position: absolute; inset: 0;
    background: linear-gradient(180deg, #1d8050 0%, #1a6e43 35%, #14573a 65%, #0c3520 100%);
  }
  .brand-mark {
    position: absolute; left: 60px; top: 136px;
    display: flex; align-items: center; gap: 12px;
    font-weight: 400; font-size: 26px; letter-spacing: 1px;
  }
  .brand-mark__dot { width: 18px; height: 18px; border-radius: 50%; background: var(--white); }
  .company-name {
    position: absolute; left: 52px; top: 176px;
    font-weight: 700; font-size: 60px; line-height: 72px; letter-spacing: 0.5px; white-space: nowrap;
  }
  .divider { position: absolute; height: 1px; background: currentColor; }
  .divider__pill { position: absolute; top: -5px; height: 10px; border-radius: 5px; background: currentColor; }
  .brand-panel .divider { left: 52px; top: 341px; width: 180px; }
  .brand-panel .divider__pill { left: 21px; width: 57px; }
  .tagline {
    position: absolute; left: 51px; top: 368px;
    font-weight: 700; font-size: 27px; letter-spacing: 0.3px;
  }
  .services {
    position: absolute; left: 52px; top: 575px; width: 380px;
    font-family: "Montserrat", Arial, sans-serif; font-weight: 500; font-size: 13.5px; line-height: 17.6px;
  }
  .website {
    position: absolute; left: 52px; top: 660px;
    font-family: "Montserrat", Arial, sans-serif; font-weight: 700; font-size: 23px; letter-spacing: 2.6px;
  }

  /* Right deal panel */
  .deal-panel {
    position: absolute; left: 490px; top: 0; width: 574px; height: 715px; overflow: hidden;
  }
  .deal-panel__photo {
    position: absolute; inset: 0;
    background: linear-gradient(180deg, var(--white) 0%, var(--photo-grey-light) 35%, var(--photo-grey-mid) 100%);
  }
  .offer-label {
    position: absolute; left: 45px; top: 34px;
    font-family: "Montserrat", Arial, sans-serif; font-weight: 700; font-size: 14px;
    letter-spacing: 2px; text-transform: uppercase; color: var(--label-green);
  }
  .headline { position: absolute; left: 45px; top: 68px; line-height: 54px; font-size: 51px; }
  .headline__lead { display: block; font-weight: 400; color: var(--ink); }
  .headline__strong { display: block; font-weight: 700; color: var(--band-green); }
  .deal-panel .divider { left: 45px; top: 197px; width: 190px; color: var(--band-green); }
  .deal-panel .divider__pill { left: 21px; width: 51px; }
  .deal-terms {
    position: absolute; left: 45px; top: 220px; list-style: none;
    font-family: "Montserrat", Arial, sans-serif; font-weight: 600; font-size: 22.3px; color: var(--ink);
  }
  .deal-terms li { height: 49px; line-height: 49px; white-space: nowrap; }
  .deal-terms .term-label { color: var(--label-green); font-weight: 700; }

  .call-band {
    position: absolute; left: 0; bottom: 0; width: 574px; height: 81px;
    background: var(--band-green); color: var(--white);
    display: flex; align-items: center; padding-left: 24px; gap: 14px;
  }
  .call-band__lead { font-size: 24px; font-weight: 400; }
  .call-band__number { font-size: 45px; font-weight: 700; letter-spacing: -0.5px; }
</style>
</head>
<body>
  <main class="brochure">
    <section class="brand-panel">
      <div class="brand-panel__photo" role="img" aria-label="Green-toned photo of a businessman climbing stairs towards a Sydney city skyline"></div>
      <div class="brand-mark"><span class="brand-mark__dot"></span>Ferngate Lending</div>
      <h1 class="company-name">FERNGATE<br>LENDING, INC.</h1>
      <div class="divider"><span class="divider__pill"></span></div>
      <p class="tagline">FINANCIAL SERVICES</p>
      <p class="services">Factor Financing, Accounts Receivable Financing, Purchase Order Financing, Contract Financing, Construction Financing, and Business Financing Attainment.</p>
      <p class="website">www.ferngatelending.com</p>
    </section>

    <section class="deal-panel">
      <div class="deal-panel__photo" role="img" aria-label="Faded grey photo of Sydney residential towers and city skyline"></div>
      <p class="offer-label">New Offering from Ferngate Lending</p>
      <h2 class="headline">
        <span class="headline__lead">We did.</span>
        <span class="headline__strong">Just last week.</span>
      </h2>
      <div class="divider"><span class="divider__pill"></span></div>
      <ul class="deal-terms">
        <li><span class="term-label">Loan Amount:</span> $750,000</li>
        <li><span class="term-label">Rate:</span> 7.79%</li>
        <li><span class="term-label">Term:</span> 12 months</li>
        <li><span class="term-label">LVR:</span> 60%</li>
        <li><span class="term-label">Repayments:</span> Capitalised</li>
        <li><span class="term-label">Security:</span> 2x Sydney Residential Propetties</li>
        <li><span class="term-label">Purpose:</span> Business Working Capital</li>
      </ul>
      <div class="call-band">
        <span class="call-band__lead">Call Mara today on</span>
        <span class="call-band__number">1-303-555-0148</span>
      </div>
    </section>
  </main>
</body>
</html>
```